Building company with a modern and unique product looking for a business card to help us stand out

We currently have a logo but as our business has grown, we feel that our business card is not reflecting our modern and high quality product and help us stand out from the crowd. Our business is mainly in the construction of new homes using a unique method and materials that makes our homes fire proof, vermin and pest resistant and rated to the maximum cyclone category (category 5). We need a business card that helps us stand out as well as communicating professionalism, high quality and trustworthiness. I have attached our current logo with a black and white option, as well as our business card which is double sided. We would like to retain as much of the information that is currently on our business cards, but presented in a more sleek way. We do like our current colour palette ( white, black, yellow and grey) and have been looking primarily at business cards with a black background however we are open to other combinations of colour and layout as long as we stand out. Please feel free to tweak our logo to make it more suitable for a business card, we like the black option that we use but we have had trouble trying to get the white area to match the rest of the logo and blend effectively into a business card. Please do not hesitate to contact us with any questions as we really want this to be successful!

Target Market(s)

Large contracts including government and larger companies

Industry/Entity Type

Business

We will be providing this business card to potential clients including key government ministers and large funding companies, our business card should show that we are professional and reliable.

Requirements
Must have
• It must be easy to read and pleasing to the eye, It must contain as much of the information on the current business card and unless something really stands out, we will most likely pick a design that has all of the information included. It must include our logo of course and have some colour included.
Nice to have
• We are looking for a high end business card and would like to see designs that reflect this. We like the gloss/matte contrast, plastic cards with opaque/coloured areas and unique features not seen on everyday paper business cards. It would be nice to see a few different colour combinations, we are open to new ideas so please feel free to take some artistic licence.
Should not have
• Must not be too busy, difficult to read or be distracting from the information conveyed. Other than this please feel free to add your own touches and make it unique!

```html
<!DOCTYPE html>
<html lang="en">
<head>
<meta charset="utf-8">
<title>Ardent Building Company – Business Card</title>
<link rel="stylesheet" href="https://fonts.googleapis.com/css2?family=Open+Sans:wght@400;600;700&display=swap">
<style>
  :root {
    --page-bg: #e9e6e1;
    --card-black: #0b0b0b;
    --card-black-edge: #1f1f1f;
    --card-white: #ffffff;
    --gold: #c9a227;
    --gold-soft: #b89a3a;
    --grey: #9a9a9a;
    --grey-dark: #555555;
    --ink: #1b1b1b;
    --text-light: #f4f4f4;
  }
  * { box-sizing: border-box; margin: 0; padding: 0; }
  html, body {
    width: 1200px; height: 913px; overflow: hidden;
    background: var(--page-bg);
    font-family: "Open Sans", Arial, sans-serif;
  }
  .sheet {
    width: 1200px; height: 913px;
    display: flex; flex-direction: column;
    align-items: center; justify-content: center; gap: 60px;
  }
  .card {
    width: 640px; height: 366px;
    border-radius: 22px;
    position: relative;
    display: flex; align-items: center;
    padding: 0 44px;
    box-shadow: 0 10px 28px rgba(0,0,0,.22);
  }
  .card--front {
    background: linear-gradient(160deg, var(--card-black-edge) 0%, var(--card-black) 45%, var(--card-black) 100%);
    color: var(--text-light);
  }
  .card--back {
    background: var(--card-white);
    color: var(--ink);
  }
  .brand {
    width: 290px;
    display: flex; align-items: center; gap: 12px;
  }
  .brand__mark {
    width: 14px; height: 14px; background: var(--gold); flex: none;
  }
  .brand__name {
    font-weight: 600; font-size: 30px; line-height: 1.1;
  }
  .card--front .brand__name { color: var(--text-light); }
  .card--back .brand__name { color: var(--gold-soft); }
  .divider {
    width: 1px; height: 190px; margin: 0 30px 0 10px;
    background: linear-gradient(180deg, transparent, var(--gold), transparent);
  }
  .card--back .divider {
    background: linear-gradient(180deg, transparent, var(--grey), transparent);
  }
  .contact { display: flex; flex-direction: column; }
  .contact__name { font-weight: 700; font-size: 24px; }
  .contact__role { font-size: 14px; color: var(--grey); margin-bottom: 16px; }
  .contact__abn { font-size: 15px; margin-bottom: 10px; }
  .contact__row {
    display: flex; align-items: center; gap: 8px;
    font-size: 15px; line-height: 1.55;
  }
  .contact__row svg { width: 13px; height: 13px; flex: none; }
  .features { list-style: none; }
  .features li {
    display: flex; align-items: center; gap: 10px;
    font-size: 16px; line-height: 1.55; color: var(--grey-dark);
  }
  .features li::before {
    content: ""; width: 13px; height: 13px; border-radius: 50%;
    background: var(--gold); flex: none;
  }
</style>
</head>
<body>
<main class="sheet">
  <section class="card card--front" aria-label="Card front">
    <div class="brand">
      <span class="brand__mark"></span>
      <span class="brand__name">Ardent Building Company</span>
    </div>
    <div class="divider"></div>
    <div class="contact">
      <span class="contact__name">Marcus Ellery</span>
      <span class="contact__role">Managing Director</span>
      <span class="contact__abn">ABN: 12 345 678 901</span>
      <span class="contact__row">
        <svg viewBox="0 0 16 16" aria-hidden="true"><path d="M3 1l3 3-1.5 2a9 9 0 0 0 5.5 5.5L12 10l3 3-2 2C7 15 1 9 1 3z" fill="none" stroke="currentColor" stroke-width="1.4"/></svg>
        0400 123 456
      </span>
      <span class="contact__row">
        <svg viewBox="0 0 16 16" aria-hidden="true"><path d="M1 6c4-4 10-4 14 0l-2 2-2-1V5H5v2L3 8z M3 10h10v5H3z" fill="none" stroke="currentColor" stroke-width="1.3"/></svg>
        (02) 5550 1234
      </span>
      <span class="contact__row">
        <svg viewBox="0 0 16 16" aria-hidden="true"><rect x="1" y="3" width="14" height="10" fill="none" stroke="currentColor" stroke-width="1.3"/><path d="M1 3l7 6 7-6" fill="none" stroke="currentColor" stroke-width="1.3"/></svg>
        hello@ardentbuilding.com
      </span>
    </div>
  </section>

  <section class="card card--back" aria-label="Card back">
    <div class="brand">
      <span class="brand__mark"></span>
      <span class="brand__name">Ardent Building Company</span>
    </div>
    <div class="divider"></div>
    <ul class="features">
      <li>Specialising in</li>
      <li>Homes that are</li>
      <li>Fire Proof</li>
      <li>Climate Proof</li>
      <li>Cyclone Rated (Cat. 5)</li>
    </ul>
  </section>
</main>
</body>
</html>
```